In need a simple business/calling card

I am looking for a VERY simple, professional, and classic business card which is really more of a calling card. In the Hartwell & Pryce or Lorvik kind of style. I am also open to a solid boarder but not necessary. I prefer no logos or "designs".

Target Market(s)

general

Contact Information for Business Card

Daniel Whitcombe (or Daniel R. Whitcombe)
+1 555 274 8163
dan@whitcombe.example

Thats it!

Font styles to use
Serif
Sans Serif
Script

Colors

Designer to choose colors to be used in the design.

Requirements
Must have
• everything on the card details section.
Nice to have
• n/a
Should not have
• No logos.

```html
<!DOCTYPE html>
<html lang="en">
<head>
<meta charset="utf-8">
<title>Daniel Whitcombe — Calling Card</title>
<link rel="stylesheet" href="https://fonts.googleapis.com/css2?family=Alegreya:wght@400;700&display=swap">
<style>
  :root {
    --backdrop: #efeeec;
    --card-navy: #1d2139;
    --ink-pearl: #dcd5d4;
  }
  html, body {
    margin: 0;
    padding: 0;
    width: 1200px;
    height: 1000px;
    overflow: hidden;
    background: var(--backdrop);
  }
  .canvas {
    position: relative;
    width: 1200px;
    height: 1000px;
  }
  .calling-card {
    position: absolute;
    left: 207px;
    top: 277px;
    width: 788px;
    height: 448px;
    background: var(--card-navy);
    color: var(--ink-pearl);
    font-family: "Alegreya", Georgia, serif;
  }
  .name-rule {
    position: absolute;
    left: 192px;
    width: 400px;
    height: 4px;
  }
  .name-rule--top { top: 153px; }
  .name-rule--bottom { top: 251px; }
  .name-rule polygon { fill: var(--ink-pearl); }
  .card-name {
    position: absolute;
    left: 0;
    right: 0;
    top: 160px;
    margin: 0;
    text-align: center;
    font-size: 66px;
    line-height: 80px;
    font-weight: 400;
    letter-spacing: 0.2px;
  }
  .card-name .surname { font-weight: 700; }
  .card-contact {
    position: absolute;
    left: 0;
    right: 0;
    top: 388px;
    margin: 0;
    text-align: center;
    font-size: 25px;
    line-height: 32px;
    letter-spacing: 0.6px;
    white-space: nowrap;
  }
  .contact-label { font-weight: 400; }
  .contact-value { font-weight: 700; }
  .contact-gap { display: inline-block; width: 20px; }
</style>
</head>
<body>
<div class="canvas">
  <section class="calling-card">
    <svg class="name-rule name-rule--top" viewBox="0 0 400 4" preserveAspectRatio="none" aria-hidden="true">
      <polygon points="0,2 200,0.4 400,2 200,3.6"/>
    </svg>
    <h1 class="card-name">Daniel <span class="surname">Whitcombe</span></h1>
    <svg class="name-rule name-rule--bottom" viewBox="0 0 400 4" preserveAspectRatio="none" aria-hidden="true">
      <polygon points="0,2 200,0.4 400,2 200,3.6"/>
    </svg>
    <p class="card-contact">
      <span class="contact-label">phone:</span> <span class="contact-value">+1 555 274 8163</span><span class="contact-gap"></span><span class="contact-label">email:</span> <span class="contact-value">dan@whitcombe.example</span>
    </p>
  </section>
</div>
</body>
</html>
```